New Business Card Design Project

2 sided business card required. I have attached some previous designs of items we have had made so you can see the logo etc. we Want the card to look professional and modern. for the final design upload for winning designer please note I need to be able to edit the names / phone numbers on the card design as I need to get them made for different staff.
Updates

extending time so designers can have time to submit

Target Market(s)

new customers

Industry/Entity Type

transport / earthmoving

Contact Information for Business Card

name, phone number email address

Requirements
Nice to have
• professional / impressive looking card (first impressions to customers count)
Should not have
• do not put our mobile number on the design use a generic number

```html
<!DOCTYPE html>
<html lang="en">
<head>
<meta charset="utf-8">
<title>KDR Pty Ltd – Business Card</title>
<link href="https://fonts.googleapis.com/css2?family=Arimo:wght@700&display=swap" rel="stylesheet">
<style>
  :root {
    --ink: #060708;
    --paper: #ffffff;
    --steel-light: #9ea3a4;
    --steel-mid: #4a4d4f;
    --steel-dark: #0b0b0c;
  }
  html, body {
    margin: 0;
    padding: 0;
    width: 1035px;
    height: 1200px;
    overflow: hidden;
    background: var(--paper);
  }
  .card {
    position: relative;
    width: 1035px;
    height: 1200px;
    font-family: "Arimo", Arial, sans-serif;
    font-weight: 700;
    color: var(--paper);
  }
  .card-front {
    position: absolute;
    left: 0;
    top: 0;
    width: 1035px;
    height: 575px;
    overflow: hidden;
  }
  .metal-texture {
    position: absolute;
    inset: 0;
    background: radial-gradient(ellipse 60% 70% at 50% 52%, var(--steel-light) 0%, var(--steel-mid) 40%, var(--steel-dark) 85%);
  }
  .brand-name {
    position: absolute;
    left: 0;
    right: 0;
    top: 178px;
    text-align: center;
    font-size: 200px;
    line-height: 1;
    letter-spacing: 4px;
    color: var(--paper);
  }
  .brand-suffix {
    position: absolute;
    left: 840px;
    top: 358px;
    font-size: 35px;
    line-height: 1;
    color: var(--paper);
  }
  .divider-band {
    position: absolute;
    left: 0;
    top: 575px;
    width: 1035px;
    height: 49px;
    background: var(--paper);
  }
  .card-back {
    position: absolute;
    left: 0;
    top: 624px;
    width: 1035px;
    height: 576px;
    background: var(--ink);
  }
  .services {
    position: absolute;
    left: 0;
    right: 0;
    top: 49px;
    margin: 0;
    padding: 0;
    list-style: none;
    text-align: center;
    font-size: 25px;
    line-height: 33.6px;
  }
  .contact {
    position: absolute;
    left: 0;
    right: 0;
    top: 482px;
    margin: 0;
    text-align: center;
    font-size: 35px;
    line-height: 42px;
  }
</style>
</head>
<body>
  <div class="card">
    <section class="card-front">
      <div class="metal-texture" role="img" aria-label="Dark perforated metal texture background"></div>
      <div class="brand-name">KDR</div>
      <div class="brand-suffix">Pty Ltd</div>
    </section>
    <div class="divider-band"></div>
    <section class="card-back">
      <ul class="services">
        <li>Over size loads / Hot Shot loads</li>
        <li>Heavy Vehicle Recovery services</li>
        <li>Potable Water Deliveries</li>
        <li>Road Building / Maintenance</li>
        <li>Earthworks</li>
        <li>Sand &amp; Metal Supply &amp; Cartage</li>
        <li>Road Train Tippers</li>
        <li>Road Train Tankers</li>
        <li>Road Train Flat Tops</li>
        <li>Drop Deck Trailers</li>
        <li>Mine site accredited</li>
        <li>equipments &amp; Operators</li>
      </ul>
      <p class="contact">Dale Harper - phone 040 555 0192</p>
    </section>
  </div>
</body>
</html>
```